We need a single page A4, single sided pdf brochure to promote our business to other businesses. Parcelo Back provides international returns solutions to on line retailers. This includes local return addresses and labels to allow customers to quickly and easily send their unwarted items back. we hen ship the returns back in bulk to the retailer.

```html
<!DOCTYPE html>
<html lang="en">
<head>
<meta charset="utf-8">
<title>Parcelo Back – International Returns Solutions</title>
<link href="https://fonts.googleapis.com/css2?family=Open+Sans:wght@300;400;600;700;800&display=swap" rel="stylesheet">
<style>
  :root {
    --backdrop: #d9d9d9;
    --ink: #1a1a1a;
    --dark: #1e1b18;
    --orange: #ee9a16;
    --white: #ffffff;
    --paper: #ffffff;
    --soft-grey: #efefef;
    --body-grey: #333333;
  }
  * { box-sizing: border-box; margin: 0; padding: 0; }
  html, body {
    width: 1200px; height: 2250px; overflow: hidden;
    background: var(--backdrop);
    font-family: "Open Sans", Arial, sans-serif;
  }
  .flyer {
    position: absolute; left: 50px; top: 347px;
    width: 1100px; height: 1556px;
    background: var(--paper);
    box-shadow: 0 6px 30px rgba(0,0,0,.18);
    overflow: hidden;
  }

  /* Header */
  .hero {
    position: relative; height: 607px; background: var(--dark);
    color: var(--white); padding: 90px 0 0 101px;
  }
  .hero-photo {
    position: absolute; right: 0; top: 0; width: 560px; height: 607px;
    background: radial-gradient(ellipse at 55% 40%, #4a4540 0%, #2c2825 55%, var(--dark) 100%);
    opacity: .9;
  }
  .hero > *:not(.hero-photo) { position: relative; }
  .brand {
    display: flex; align-items: center; gap: 18px;
    font-weight: 800; font-size: 58px; letter-spacing: 1px; line-height: 1;
  }
  .brand-square { width: 40px; height: 40px; background: var(--orange); }
  .hero-title {
    margin-top: 58px; font-weight: 300; font-size: 55px; line-height: 1.1;
  }
  .hero-title strong {
    display: block; font-weight: 700; color: var(--orange); margin-top: 6px;
  }
  .hero-rule { width: 60px; height: 7px; background: var(--white); margin: 34px 0 36px; border-radius: 4px; }
  .hero-lead { font-weight: 600; font-size: 28px; line-height: 1.38; max-width: 680px; }
  .hero-challenge { margin-top: 20px; font-weight: 600; font-size: 27px; color: var(--orange); }

  /* Services */
  .services { height: 303px; padding: 40px 0 0 101px; color: var(--ink); }
  .services h2 { font-weight: 700; font-size: 25px; line-height: 34px; white-space: nowrap; margin-bottom: 14px; }
  .service-list { list-style: none; }
  .service-list li {
    display: flex; align-items: center; gap: 20px;
    font-size: 24px; line-height: 37px;
  }
  .bullet-square { width: 15px; height: 15px; background: var(--orange); flex: none; }

  /* Orange band */
  .solutions {
    height: 365px; background: var(--orange); color: var(--white);
    display: flex; padding: 24px 0 0 101px;
  }
  .solution-col { width: 468px; }
  .solution-col h3 { font-weight: 400; font-size: 34px; line-height: 1.2; color: var(--ink); }
  .solution-col h3 b { font-weight: 700; color: var(--white); }
  .mini-rule { width: 26px; height: 5px; background: var(--white); margin: 6px 0 18px; border-radius: 3px; }
  .solution-list { list-style: none; }
  .solution-list li {
    display: flex; gap: 14px; font-size: 20px; line-height: 27px; margin-bottom: 8px; color: var(--ink);
  }
  .solution-list .bullet-square { width: 12px; height: 12px; background: var(--white); margin-top: 8px; }
  .footnote { font-size: 12px; color: var(--ink); margin-top: 6px; }

  .contact-col { padding-top: 2px; }
  .contact-col h3 { font-weight: 700; font-size: 36px; line-height: 1.1; margin-bottom: 10px; }
  .contact-note { font-size: 18px; line-height: 1.3; color: #fff7e6; margin-bottom: 2px; }
  .contact-line { display: flex; align-items: center; gap: 14px; font-weight: 700; font-size: 29px; line-height: 1.25; margin-bottom: 10px; }
  .contact-line svg { flex: none; }
  .phone-line { font-size: 35px; margin-top: 6px; margin-bottom: 0; }
  .flags { display: flex; gap: 6px; margin: 4px 0 4px; }
  .flag { width: 34px; height: 22px; display: block; }

  /* About */
  .about { height: 281px; background: var(--soft-grey); padding: 32px 101px 0 101px; color: var(--body-grey); }
  .about h3 { font-weight: 400; font-size: 32px; line-height: 1.2; color: var(--ink); }
  .about h3 b { font-weight: 700; color: var(--orange); }
  .about .mini-rule { background: var(--orange); margin: 4px 0 16px; }
  .about p { font-size: 17px; line-height: 1.5; margin-bottom: 18px; }
</style>
</head>
<body>
  <article class="flyer">
    <header class="hero">
      <div class="hero-photo" role="img" aria-label="Photo of a hand holding a smartphone showing an online shoe shop"></div>
      <div class="brand"><span class="brand-square"></span>PARCELO BACK</div>
      <h1 class="hero-title">International Returns Solutions for<strong>On-Line Retailers</strong></h1>
      <div class="hero-rule"></div>
      <p class="hero-lead">Selling internationally brings opportunities and challenges to retailers of all sizes.</p>
      <p class="hero-challenge">One of those challenges is how to deal effectively with customer returns.</p>
    </header>

    <section class="services">
      <h2>Parcelo Back have a range of services to suit retailers of all sizes that will:</h2>
      <ul class="service-list">
        <li><span class="bullet-square"></span>Lower your returns costs – Save you and your customers money</li>
        <li><span class="bullet-square"></span>Improve your customers experience – Better feedback &amp; ratings</li>
        <li><span class="bullet-square"></span>Add value to your international business – More Sales</li>
        <li><span class="bullet-square"></span>Save time on managing International Returns – Less Administration</li>
        <li><span class="bullet-square"></span>Help you comply with marketplace International Return policies and best practice</li>
      </ul>
    </section>

    <section class="solutions">
      <div class="solution-col">
        <h3>Our Solution <b>includes:</b></h3>
        <div class="mini-rule"></div>
        <ul class="solution-list">
          <li><span class="bullet-square"></span>Local Returns Addresses in 9 Countries*</li>
          <li><span class="bullet-square"></span>Return Label solutions in over 20 other countries*</li>
          <li><span class="bullet-square"></span>Your own dedicated &amp; branded<br>Label Portal</li>
          <li><span class="bullet-square"></span>Parcelo Back Retailer Portal to monitor and manage your returns</li>
        </ul>
        <p class="footnote">*Please see our website for an up-to-date list of countries we operate in.</p>
      </div>
      <div class="contact-col">
        <h3>Interested?</h3>
        <p class="contact-note">See our website for more information</p>
        <p class="contact-line">
          <svg width="26" height="26" viewBox="0 0 26 26" fill="none" stroke="#fff" stroke-width="2.4"><circle cx="13" cy="13" r="11"/><ellipse cx="13" cy="13" rx="5" ry="11"/><line x1="2" y1="13" x2="24" y2="13"/></svg>
          www.parceloback.com
        </p>
        <p class="contact-note">or contact us to discuss how we can work together.</p>
        <p class="contact-line">
          <svg width="26" height="20" viewBox="0 0 26 20" fill="none" stroke="#fff" stroke-width="2.4"><rect x="1.5" y="1.5" width="23" height="17"/><polyline points="1.5,1.5 13,11 24.5,1.5"/></svg>
          info@parceloback.com
        </p>
        <p class="contact-note">Write to us in these languages</p>
        <div class="flags">
          <svg class="flag" viewBox="0 0 34 22"><rect width="34" height="22" fill="#b22234"/><rect y="3" width="34" height="3" fill="#fff"/><rect y="9" width="34" height="3" fill="#fff"/><rect y="15" width="34" height="3" fill="#fff"/><rect width="15" height="12" fill="#3c3b6e"/></svg>
          <svg class="flag" viewBox="0 0 34 22"><rect width="34" height="8" fill="#ae1c28"/><rect y="7" width="34" height="8" fill="#fff"/><rect y="15" width="34" height="7" fill="#21468b"/></svg>
          <svg class="flag" viewBox="0 0 34 22"><rect width="34" height="22" fill="#aa151b"/><rect y="6" width="34" height="10" fill="#f1bf00"/></svg>
          <svg class="flag" viewBox="0 0 34 22"><rect width="12" height="22" fill="#0055a4"/><rect x="11" width="12" height="22" fill="#fff"/><rect x="22" width="12" height="22" fill="#ef4135"/></svg>
        </div>
        <p class="contact-line phone-line">
          <svg width="32" height="32" viewBox="0 0 32 32" fill="none" stroke="#fff" stroke-width="2.6"><circle cx="16" cy="16" r="14"/><path d="M11 9 l3 0 l1.5 4 l-2 1.5 a9 9 0 0 0 4 4 l1.5 -2 l4 1.5 l0 3 a2 2 0 0 1 -2 2 a14 14 0 0 1 -12 -12 a2 2 0 0 1 2 -2z" fill="#fff" stroke="none"/></svg>
          +44(0)161 555 0148
        </p>
      </div>
    </section>

    <section class="about">
      <h3>About <b>Us</b></h3>
      <div class="mini-rule"></div>
      <p>Parcelo Back is a fast growing family-run business that has been providing International return services to on line sellers since 2015. Through our UK and French based businesses, together with our trusted partner network, we deliver a service that saves retailers money and time.</p>
      <p>The owners of Parcelo Back come from a retail and e-commerce background, so we fully understand and appreciate the issues and challenges faced by retailers, as well as the concerns of customers when it comes to returns.</p>
    </section>
  </article>
</body>
</html>
```